Wix web design for healthcare IT consulting firm.

I am looking for a web design built in Wix that it will be easy for me to add or edit content in the future. The web site does not need to be overly complicated, but it should look very polished and professional. I also want to ensure it is mobile device friendly. I do not need any type of on-line purchasing ability. I will eventually do blogs, but for now it is a fairly standard web site with main page, about us, services provided, etc. I would also like a place for potential customers to contact us directly from the web site. I have included a Word document with some content for the web design. I have also included my logo and business card for reference. I would like to utilize similar colors as my business card. One of my primary competitors is https://vonmarlhq.example/

Target Market(s)

Target market could be nursing home CEO, CIO, or other leader at an organization that manages long term care facilities.

Number of Pages Required

5+ page

Colors
876aae

Requirements
Must have
• Be designed to be used in Wix. Use the content I provided to create and make web design. Allow to be viewed on mobile device. Please use similar color structure as attached business card. Please use attached logo in design.

```html
<!DOCTYPE html>
<html lang="en">
<head>
<meta charset="utf-8">
<title>Quillane HealthCare Solutions</title>
<link href="https://fonts.googleapis.com/css2?family=Open+Sans:wght@300;400;600;700&display=swap" rel="stylesheet">
<style>
:root{
  --purple:#8a6bbf;
  --purple-bright:#9b6fd6;
  --purple-deep:#7c4fc2;
  --panel-1:#9d7fd1;
  --panel-2:#8f66cc;
  --panel-3:#8a47cf;
  --ink:#2f2f35;
  --muted:#8d8d96;
  --line:#e4e1ea;
  --footer:#ebebee;
  --white:#ffffff;
}
*{box-sizing:border-box;margin:0;padding:0}
html,body{width:1200px;height:2520px;overflow:hidden}
body{font-family:"Open Sans",Arial,sans-serif;color:var(--ink);background:var(--white);position:relative}
.abs{position:absolute}

/* Header */
.site-header{position:absolute;left:0;top:0;width:1200px;height:73px;background:var(--white)}
.brand{position:absolute;left:207px;top:14px;display:flex;align-items:center;gap:10px}
.brand-mark{width:14px;height:14px;background:var(--purple)}
.brand-name{font-size:22px;font-weight:700;color:var(--purple);line-height:1}
.main-nav{position:absolute;right:207px;top:22px;display:flex;align-items:center;gap:34px;font-size:14px}
.main-nav a{color:var(--ink);text-decoration:none}
.main-nav a.active{color:var(--purple);font-weight:700}
.main-nav .nav-cta{background:var(--purple);color:var(--white);padding:6px 14px}

/* Hero */
.hero{position:absolute;left:0;top:73px;width:1200px;height:469px;background:linear-gradient(100deg,#c9c9cc 0%,#d9d9dc 45%,#ececee 75%,#f1f1f3 100%)}
.hero-photo{position:absolute;right:0;top:0;width:420px;height:469px;background:radial-gradient(ellipse at 60% 60%,#f7f7f8 0%,#e6e8ea 45%,rgba(230,232,234,0) 75%)}
.hero-title{position:absolute;left:205px;top:120px;font-size:39px;font-weight:700;color:var(--purple-bright);line-height:1.1;white-space:nowrap}
.hero-subtitle{position:absolute;left:205px;top:158px;font-size:30px;font-weight:600;color:var(--white);white-space:nowrap}
.hero-text{position:absolute;left:205px;top:207px;width:440px;font-size:14px;line-height:18px;color:var(--white)}
.btn-outline{position:absolute;left:205px;top:342px;width:155px;height:52px;border:3px solid var(--purple);color:var(--purple);font-weight:700;font-size:17px;display:flex;align-items:center;justify-content:center}

/* Section headings */
.eyebrow{position:absolute;left:207px;font-size:9px;font-weight:700;color:var(--purple);letter-spacing:.5px;text-transform:uppercase}
.section-title{position:absolute;left:205px;font-size:22px;font-weight:400;color:var(--ink)}

/* Services */
.service-menu{position:absolute;left:207px;top:658px;width:197px;height:193px;background:var(--panel-1);color:var(--white);box-shadow:0 4px 10px rgba(0,0,0,.12)}
.service-menu h3{font-size:16px;font-weight:300;line-height:21px;padding:18px 16px 18px}
.service-menu .menu-item{font-size:12px;font-weight:300;padding:0 16px;height:32px;display:flex;align-items:center;justify-content:space-between;border-top:1px solid rgba(255,255,255,.35)}
.service-intro{position:absolute;left:415px;top:660px;width:340px;font-size:10.5px;line-height:14px;color:var(--muted)}
.slider-arrows{position:absolute;left:966px;top:668px;display:flex;gap:2px}
.slider-arrows span{width:13px;height:13px;border:1px solid #c9c4d2}
.service-card{position:absolute;top:705px;width:138px}
.service-card .photo{height:86px;background:linear-gradient(135deg,#6e7078,#c8cad0)}
.service-card h4{font-size:10.5px;font-weight:400;color:var(--purple);margin-top:6px}
.service-card p{font-size:9.5px;line-height:12px;color:var(--muted);margin-top:3px}

/* Advantages */
.advantage{position:absolute;top:1050px;width:190px}
.advantage .icon{width:76px;height:76px;border-radius:8px;background:linear-gradient(135deg,#efe8f8,#e2d6f3)}
.advantage h4{font-size:14px;font-weight:400;color:var(--ink);margin-top:22px}
.advantage p{font-size:11px;line-height:14px;color:var(--muted);margin-top:10px}

/* Testimonials */
.testimonials{position:absolute;left:0;top:1293px;width:1200px;height:372px;background:linear-gradient(90deg,#c6cbd6 0%,#dfe2e9 35%,#dde0e6 60%,#b7bcc6 100%)}
.testimonials .eyebrow{top:24px}
.testimonials .section-title{top:36px}
.testimonial-card{position:absolute;top:89px;width:210px;height:252px;background:var(--white);box-shadow:0 3px 10px rgba(0,0,0,.15);text-align:center}
.testimonial-card .photo{height:118px;background:linear-gradient(135deg,#7f7565,#c9b79a)}
.testimonial-card h4{font-size:14px;font-weight:700;color:var(--purple);margin-top:12px}
.testimonial-card .role{font-size:9px;font-weight:700;color:var(--ink);margin-top:1px}
.testimonial-card p{font-size:9.5px;line-height:13px;color:var(--muted);padding:6px 10px 0}

/* Info panels */
.info-panel{position:absolute;top:1805px;width:262px;height:195px;color:var(--white);padding:20px 16px;box-shadow:0 6px 12px rgba(0,0,0,.12)}
.info-panel h3{font-size:16px;font-weight:400}
.info-panel p{font-size:10px;line-height:13px;margin-top:12px;opacity:.92}
.info-panel .btn-small{position:absolute;left:16px;bottom:18px;border:1px solid var(--white);font-size:10px;padding:3px 7px}

/* Mission */
.mission{position:absolute;left:0;top:2091px;width:1200px;height:209px;background:linear-gradient(180deg,#f8fafe 0%,#eaf1fb 100%);text-align:center}
.mission h2{position:absolute;left:0;width:1200px;top:68px;font-size:21px;font-weight:700;color:var(--purple)}
.mission p{position:absolute;left:0;width:1200px;top:98px;font-size:14px;color:var(--ink)}
.mission .btn-fill{position:absolute;left:524px;top:142px;width:152px;height:44px;background:var(--purple);color:var(--white);font-weight:700;font-size:14px;display:flex;align-items:center;justify-content:center}

/* Footer */
.site-footer{position:absolute;left:0;top:2300px;width:1200px;height:220px;background:var(--footer)}
.site-footer .brand{top:34px;left:207px}
.socials{position:absolute;left:236px;top:90px;display:flex;gap:14px}
.socials span{width:11px;height:11px;border-radius:50%;background:#5a5a62}
.footer-col{position:absolute;top:32px}
.footer-col h5{font-size:14px;font-weight:700;color:var(--purple);margin-bottom:10px}
.footer-col li{list-style:none;font-size:10.5px;line-height:22px;color:var(--muted)}
.footer-col li b{color:var(--purple);font-weight:600}
.copyright{position:absolute;left:0;width:1200px;top:190px;text-align:center;font-size:9.5px;color:var(--muted)}
</style>
</head>
<body>

<header class="site-header">
  <div class="brand"><span class="brand-name">Quillane</span></div>
  <nav class="main-nav">
    <a class="active" href="#">Home</a>
    <a href="#">About Us</a>
    <a href="#">Services</a>
    <a href="#">Contact Us</a>
    <a class="nav-cta" href="#">Get Started</a>
  </nav>
</header>

<section class="hero" role="img" aria-label="Photograph of scattered teal and dark green capsules beside a white medicine bottle on a light grey surface">
  <div class="hero-photo"></div>
  <h1 class="hero-title">Increasing the value and security</h1>
  <div class="hero-subtitle">of your technology resources</div>
  <p class="hero-text">We understand different organizations have different needs. Quillane HCS strives to assist your organization by bringing solutions that are easy to understand and allow the customer to track success. We provide solutions based on the customer's needs and desires.</p>
  <div class="btn-outline">Get Started</div>
</section>

<!-- Services -->
<div class="eyebrow" style="top:590px">Our Services</div>
<h2 class="section-title" style="top:600px">Solutions for your needs and desires</h2>

<div class="service-menu">
  <h3>Quillane HealthCare<br>Services</h3>
  <div class="menu-item"><span>Electronic Health Record</span><span>›</span></div>
  <div class="menu-item"><span>Information Technology</span></div>
</div>
<p class="service-intro">Quillane HCS strives to assist<br>your organization by bringing solutions that are easy to understand.</p>
<div class="slider-arrows"><span></span><span></span></div>

<div class="service-card" style="left:416px">
  <div class="photo" role="img" aria-label="Photograph of a clinician taking a blood pressure reading"></div>
  <h4>EHR Optimization Services</h4>
  <p>Lorem ipsum dolor sit amet, consectetur adipiscing elit. Integer eget luctus nisl. Aenean varius.</p>
</div>
<div class="service-card" style="left:562px">
  <div class="photo" role="img" aria-label="Photograph of a lab technician in a mask at work"></div>
  <h4>EHR Implementation</h4>
  <p>Lorem ipsum dolor sit amet, consectetur adipiscing elit. Integer eget luctus nisl. Aenean varius.</p>
</div>
<div class="service-card" style="left:711px">
  <div class="photo" role="img" aria-label="Photograph of hands reviewing medical paperwork"></div>
  <h4>EHR Assessment</h4>
  <p>Lorem ipsum dolor sit amet, consectetur adipiscing elit. Integer eget luctus nisl. Aenean varius.</p>
</div>
<div class="service-card" style="left:856px">
  <div class="photo" role="img" aria-label="Photograph of a researcher using a microscope"></div>
  <h4>EHR Quality Assessment</h4>
  <p>Lorem ipsum dolor sit amet, consectetur adipiscing elit. Integer eget luctus nisl. Aenean varius.</p>
</div>

<!-- Advantages -->
<div class="eyebrow" style="top:960px">Our Advantages</div>
<h2 class="section-title" style="top:972px">We always work hard to you with the best service</h2>

<div class="advantage" style="left:205px">
  <div class="icon" role="img" aria-label="Line icon of two people high-fiving"></div>
  <h4>Customer Focused</h4>
  <p>Lorem ipsum dolor sit amet, consectetur adipiscing elit. Integer eget luctus nisl.</p>
</div>
<div class="advantage" style="left:409px">
  <div class="icon" role="img" aria-label="Line icon of hands holding a heart"></div>
  <h4>Integrity &amp; Ethics</h4>
  <p>Lorem ipsum dolor sit amet, consectetur adipiscing elit. Integer eget luctus nisl.</p>
</div>
<div class="advantage" style="left:600px">
  <div class="icon" role="img" aria-label="Line icon of a person climbing steps"></div>
  <h4>Practice Accountability</h4>
  <p>Lorem ipsum dolor sit amet, consectetur adipiscing elit. Integer eget luctus nisl.</p>
</div>
<div class="advantage" style="left:805px">
  <div class="icon" role="img" aria-label="Line icon of joined puzzle pieces"></div>
  <h4>Professional Development</h4>
  <p>Lorem ipsum dolor sit amet, consectetur adipiscing elit. Integer eget luctus nisl.</p>
</div>

<!-- Testimonials -->
<section class="testimonials" role="img" aria-label="Blurred photograph of a doctor reviewing an x-ray">
  <div class="eyebrow">Our Testimonials</div>
  <h2 class="section-title">What our clients say</h2>

  <div class="testimonial-card" style="left:207px">
    <div class="photo" role="img" aria-label="Photograph of a smiling man on the phone at a laptop"></div>
    <h4>Dorian K. Welles</h4>
    <div class="role">CareNova CEO</div>
    <p>Lorem ipsum dolor sit amet, consectetur adipiscing elit. Integer eget luctus nisl. Maecenas fringilla consequat lacus et eleifend. Sed ultrices vitae massa eu blandit. Donec at semper.</p>
  </div>
  <div class="testimonial-card" style="left:494px">
    <div class="photo" role="img" aria-label="Photograph of a smiling woman outdoors" style="background:linear-gradient(135deg,#3f6a2f,#b9c98a)"></div>
    <h4>Linnea T. Varga</h4>
    <div class="role">CareNova Manager</div>
    <p>Lorem ipsum dolor sit amet, consectetur adipiscing elit. Integer eget luctus nisl. Maecenas fringilla consequat lacus et eleifend. Sed ultrices vitae massa eu blandit. Donec at semper.</p>
  </div>
  <div class="testimonial-card" style="left:782px">
    <div class="photo" role="img" aria-label="Photograph of a man in glasses talking on the phone" style="background:linear-gradient(135deg,#5d6b7d,#c8ccd2)"></div>
    <h4>Howard J. Pell</h4>
    <div class="role">Medrana Manager</div>
    <p>Lorem ipsum dolor sit amet, consectetur adipiscing elit. Integer eget luctus nisl. Maecenas fringilla consequat lacus et eleifend. Sed ultrices vitae massa eu blandit. Donec at semper.</p>
  </div>
</section>

<!-- Additional info -->
<div class="eyebrow" style="top:1713px">Site Materials</div>
<h2 class="section-title" style="top:1724px">Additional information you may like to know</h2>

<div class="info-panel" style="left:207px;background:var(--panel-1)">
  <h3>Our Services</h3>
  <p>Lorem ipsum dolor sit amet, consectetur adipiscing elit. Integer eget luctus nisl. Aenean varius ligula ut pellentesque sodales. Sed cursus dictum ullamcorper. Proin felis ipsum, varius ac enim ac, tristique rutrum.</p>
  <span class="btn-small">Read More</span>
</div>
<div class="info-panel" style="left:469px;background:var(--panel-2)">
  <h3>Our Team</h3>
  <p>Lorem ipsum dolor sit amet, consectetur adipiscing elit. Integer eget luctus nisl. Aenean varius ligula ut pellentesque sodales. Sed cursus dictum ullamcorper. Proin felis ipsum, varius ac enim ac, tristique rutrum.</p>
  <span class="btn-small">Read More</span>
</div>
<div class="info-panel" style="left:731px;background:var(--panel-3)">
  <h3>Contact Us</h3>
  <p>Lorem ipsum dolor sit amet, consectetur adipiscing elit. Integer eget luctus nisl. Aenean varius ligula ut pellentesque sodales. Sed cursus dictum ullamcorper. Proin felis ipsum, varius ac enim ac, tristique rutrum.</p>
  <span class="btn-small">Read More</span>
</div>

<!-- Mission -->
<section class="mission">
  <h2>OUR MISSION IS TO PARTNER WITH CUSTOMERS</h2>
  <p>To increase the value of their technology tools</p>
  <div class="btn-fill">Contact Us</div>
</section>

<!-- Footer -->
<footer class="site-footer">
  <div class="brand"><span class="brand-name">Quillane</span></div>
  <div class="socials"><span></span><span></span><span></span></div>

  <div class="footer-col" style="left:436px">
    <h5>Our Services</h5>
    <ul>
      <li>Risk Assessment</li>
      <li>Policy Management</li>
      <li>Chief Information Officer</li>
      <li>Chief Information Security Officer</li>
      <li>IRT Department Evaluation</li>
    </ul>
  </div>
  <div class="footer-col" style="left:631px;top:57px">
    <ul>
      <li>EHR Optimization Services</li>
      <li>EHR Implementation</li>
      <li>EHR Assessment</li>
      <li>EHR Quality Assessment</li>
      <li>EHR Quality Assessment</li>
    </ul>
  </div>
  <div class="footer-col" style="left:798px">
    <h5>Contact Us</h5>
    <ul>
      <li>Email us: <b>info@quillanehcs.example</b></li>
      <li>Call us: <b>555-014-2290</b></li>
    </ul>
  </div>
  <div class="copyright">©Quillane HealthCare. All Rights Reserved.</div>
</footer>

</body>
</html>
```